Website design for commercial and residential security company

we're looking to see some new designs for an established company with no website.

homepage and one inner page

here is a link to the homepage content, sitemap, logo and more.
https://files.brontavel.net/share/7QxmPzLrTw2vNkdJhYcsa9eFgbUoiVwRn?view=open

call to action should be Request A Quote

if you have any questions please send them to us asap

thank you

1 page

Sans Serif

```html
<!DOCTYPE html>
<html lang="en">
<head>
<meta charset="UTF-8">
<title>Beacon Ridge Security Group</title>
<link href="https://fonts.googleapis.com/css2?family=Montserrat:wght@400;500;600;700;800&display=swap" rel="stylesheet">
<style>
:root{
  --navy:#0d1a4f;
  --navy-deep:#081238;
  --gold:#d4af2c;
  --gold-soft:#e2c24a;
  --ink:#1b1b1b;
  --muted:#555b66;
  --white:#ffffff;
}
*{box-sizing:border-box;margin:0;padding:0}
html,body{width:1200px;height:4124px;overflow:hidden}
body{font-family:'Montserrat',sans-serif;color:var(--ink);background:var(--white);position:relative}
.abs{position:absolute}

/* header */
.site-header{position:absolute;top:0;left:0;width:1200px;height:64px;background:rgba(255,255,255,.96);z-index:3;display:flex;align-items:center;padding:0 112px}
.brand{display:flex;align-items:center;gap:10px;font-weight:800;font-size:17px;color:var(--navy);letter-spacing:.5px}
.brand-dot{width:14px;height:14px;border-radius:50%;background:var(--gold)}
.nav{margin-left:auto;display:flex;gap:34px;font-size:13px;font-weight:600;color:var(--navy)}
.nav .active{color:var(--gold)}

/* hero */
.hero{top:0;left:0;width:1200px;height:760px;background:linear-gradient(110deg,#0a1230 0%,#1b2c6b 45%,#0f1a48 100%)}
.hero-title{left:612px;top:370px;color:var(--white);font-size:44px;line-height:1.15;text-transform:uppercase}
.hero-title .light{font-weight:400;color:var(--gold-soft)}
.hero-title .bold{font-weight:800}
.btn{display:inline-block;background:var(--gold);color:var(--white);font-weight:700;font-size:13px;letter-spacing:1px;text-transform:uppercase;border-radius:30px;padding:18px 36px}
.hero .btn{position:absolute;left:612px;top:520px}
.dots{left:612px;top:688px;display:flex;gap:14px}
.dots span{width:46px;height:5px;border-radius:3px;background:rgba(255,255,255,.45)}
.dots span:first-child{background:var(--white)}

/* headings */
.section-title{font-size:40px;color:var(--ink);text-transform:uppercase;line-height:1.1}
.section-title b{font-weight:800}
.section-title span{font-weight:400}
.rule{width:60px;height:4px;background:var(--gold);margin:14px 0 26px}
.lead{font-size:17px;font-weight:600;line-height:1.55}
.body-text{font-size:15px;line-height:1.7;color:var(--muted)}

/* mission */
.mission{left:112px;top:970px;width:520px}
.photo-circle{border-radius:50%}
.mission-photo{left:680px;top:920px;width:400px;height:400px;background:radial-gradient(circle at 40% 40%,#5e7aa6,#1d2f5c)}

/* commercial */
.commercial-band{left:0;top:1380px;width:1200px}
.commercial-photo{left:-20px;top:1640px;width:520px;height:520px;background:radial-gradient(circle at 55% 45%,#3b6fb5,#0a1a45);border:10px solid var(--navy)}
.commercial{left:572px;top:1620px;width:520px;color:var(--white)}
.commercial .section-title{color:var(--white)}
.commercial .lead{color:var(--white);font-size:16px}
.commercial .body-text{color:#d6dbeb;margin-top:22px}
.ticks{list-style:none;margin-top:18px}
.ticks li{display:flex;gap:14px;font-size:15px;line-height:1.6;color:#d6dbeb;margin-bottom:14px}
.ticks svg{flex:none;margin-top:3px}
.commercial .btn{margin-top:16px}

/* residential */
.residential{left:112px;top:2500px;width:520px}
.residential .btn{margin-top:26px}
.residential-photo{left:700px;top:2450px;width:560px;height:560px;background:radial-gradient(circle at 45% 40%,#ffffff,#cfd4dc 60%,#8f97a4)}

/* contact */
.contact{left:0;top:3072px;width:1200px;height:668px;background:var(--gold)}
.contact-title{position:absolute;top:60px;width:100%;text-align:center;color:var(--white);font-size:36px;text-transform:uppercase}
.contact-title b{font-weight:700}
.contact-title span{font-weight:400}
.field{position:absolute;background:var(--white);height:56px;font-size:12px;font-weight:600;color:#666;padding:20px 14px;text-transform:uppercase}
.field.msg{height:176px}
.send{position:absolute;left:518px;top:510px;background:var(--navy);color:var(--white);font-size:12px;font-weight:700;border-radius:30px;padding:16px 40px}

/* footer */
.footer{left:0;top:3740px;width:1200px;height:340px;background:var(--navy)}
.footer .brand{position:absolute;left:112px;top:56px;color:var(--white);font-size:20px}
.contact-line{position:absolute;left:112px;display:flex;gap:12px;align-items:center;color:var(--white);font-size:14px}
.socials{position:absolute;left:112px;top:200px;display:flex;gap:14px}
.socials span{width:36px;height:36px;border-radius:50%;border:2px solid var(--gold)}
.col-title{position:absolute;top:60px;color:var(--white);font-weight:700;font-size:16px;text-transform:uppercase}
.links{position:absolute;left:508px;top:96px;list-style:none;color:#d6dbeb;font-size:14px;line-height:2.2}
.email-box{position:absolute;left:780px;top:100px;width:306px;height:52px;background:var(--white);font-size:12px;color:#777;padding:19px 18px;text-transform:uppercase}
.subscribe{position:absolute;left:780px;top:170px;width:306px;height:48px;background:var(--gold);color:var(--white);font-size:12px;font-weight:700;text-align:center;padding-top:17px;text-transform:uppercase}
.copyright{left:0;top:4080px;width:1200px;height:44px;background:var(--navy-deep);color:#c5cbe0;font-size:12px;text-align:center;padding-top:15px}
.copyright b{color:var(--gold);font-weight:600}
</style>
</head>
<body>

<header class="site-header">
  <div class="brand"><span class="brand-dot"></span>BEACON RIDGE SECURITY GROUP</div>
  <nav class="nav"><span class="active">HOME</span><span>ABOUT</span><span>SOLUTIONS ▾</span><span>RESOURCES ▾</span><span>CONTACT</span></nav>
</header>

<section class="hero abs" role="img" aria-label="Security operator watching a wall of CCTV monitors">
  <h1 class="hero-title abs"><span class="light">People's safety is</span><br><span class="bold">our top priority</span></h1>
  <span class="btn">Request a Quote</span>
  <div class="dots abs"><span></span><span></span><span></span></div>
</section>

<section class="mission abs">
  <h2 class="section-title"><b>Our</b> <span>Mission</span></h2>
  <div class="rule"></div>
  <p class="lead">To provide our customers with comprehensive security, audio/video, and automation with top notch customer service. We Ensure Security with Smart Tools.</p>
  <p class="body-text" style="margin-top:26px">The graded security measures from Beacon Ridge Security Group ensure the safety of both residential and commercial property. We provide a wide range of Residential and Commercial Security Solutions.</p>
</section>
<div class="mission-photo photo-circle abs" role="img" aria-label="Security guard speaking into a radio in front of monitors"></div>

<svg class="commercial-band abs" width="1200" height="980" viewBox="0 0 1200 980">
  <path d="M0 80 Q600 -80 1200 80 L1200 980 L0 980 Z" fill="#0d1a4f"/>
</svg>
<div class="commercial-photo photo-circle abs" role="img" aria-label="Team working at screens in a security control room"></div>
<section class="commercial abs">
  <h2 class="section-title"><b>Commercial</b> <span>Solutions</span></h2>
  <div class="rule"></div>
  <p class="lead">Protect assets and security of your business with Exceptional Commercial Security Installation</p>
  <p class="body-text">People's safety is our top priority. This includes ensuring that the security system built at your commercial property is configured accurately. Further, it will protect against intruders, burglaries, and holdups. We do this by:</p>
  <ul class="ticks">
    <li><svg width="16" height="16" viewBox="0 0 16 16"><circle cx="8" cy="8" r="8" fill="#d4af2c"/><path d="M4.5 8.2l2.3 2.3 4.7-4.8" stroke="#fff" stroke-width="1.8" fill="none"/></svg>Audio &amp; Video Solutions for your commercial property</li>
    <li><svg width="16" height="16" viewBox="0 0 16 16"><circle cx="8" cy="8" r="8" fill="#d4af2c"/><path d="M4.5 8.2l2.3 2.3 4.7-4.8" stroke="#fff" stroke-width="1.8" fill="none"/></svg>Burglar Alarms &amp; Detectors</li>
    <li><svg width="16" height="16" viewBox="0 0 16 16"><circle cx="8" cy="8" r="8" fill="#d4af2c"/><path d="M4.5 8.2l2.3 2.3 4.7-4.8" stroke="#fff" stroke-width="1.8" fill="none"/></svg>CCTV cameras equipped with facial recognition technologies enable the technology to identify the offenders.</li>
    <li><svg width="16" height="16" viewBox="0 0 16 16"><circle cx="8" cy="8" r="8" fill="#d4af2c"/><path d="M4.5 8.2l2.3 2.3 4.7-4.8" stroke="#fff" stroke-width="1.8" fill="none"/></svg>Monitoring of alarms and video recordings 24 hours a day, seven days a week. Addressing all the incidents with an urgent response.</li>
  </ul>
  <span class="btn">Read More</span>
</section>

<section class="residential abs">
  <h2 class="section-title"><b>Residential Security</b><br><span>Solutions</span></h2>
  <div class="rule"></div>
  <p class="lead" style="font-size:15px">Consider a home surveillance device that would do more for you and your family than you ever imagined.</p>
  <p class="body-text" style="margin-top:22px">Beacon Ridge Security Group is your trustable security provider. Also, as certified professionals carry out the installation, you have everything under control. Your home is being securely watched from various points, with cameras capable of tracking any intruder's path. Specifically, we offer Residential Intrusion Detection Security Systems, Residential Alarm, Residential Network Wi-Fi, CCTVs and residential home automation.</p>
  <span class="btn">Read More</span>
</section>
<div class="residential-photo photo-circle abs" role="img" aria-label="White dome security camera"></div>

<section class="contact abs">
  <h2 class="contact-title"><b>Get in touch with us</b> <span>today</span></h2>
  <div class="field" style="left:292px;top:170px;width:296px">Name</div>
  <div class="field" style="left:608px;top:170px;width:296px">Email Address</div>
  <div class="field" style="left:292px;top:244px;width:296px">Phone No</div>
  <div class="field" style="left:608px;top:244px;width:296px">Subject</div>
  <div class="field msg" style="left:292px;top:318px;width:612px">Message</div>
  <span class="send">SEND NOW</span>
</section>

<footer class="footer abs">
  <div class="brand"><span class="brand-dot"></span>BEACON RIDGE</div>
  <div class="contact-line" style="top:118px"><svg width="16" height="16" viewBox="0 0 16 16"><path d="M3 1h3l1.5 4-2 1.2a9 9 0 0 0 4.3 4.3L11 8.5l4 1.5v3a2 2 0 0 1-2 2A12 12 0 0 1 1 3a2 2 0 0 1 2-2z" fill="#d4af2c"/></svg>123-456-7890</div>
  <div class="contact-line" style="top:154px"><svg width="16" height="16" viewBox="0 0 16 16"><rect x="1" y="3" width="14" height="10" rx="1.5" fill="#d4af2c"/><path d="M1.5 4l6.5 5 6.5-5" stroke="#0d1a4f" stroke-width="1.4" fill="none"/></svg>hello@beaconridge-example.com</div>
  <div class="socials"><span></span><span></span><span></span></div>
  <div class="col-title" style="left:508px">Quick Links</div>
  <ul class="links"><li>Home</li><li>About</li><li>Solutions</li><li>Resources</li><li>Contact</li></ul>
  <div class="col-title" style="left:780px">Newsletter</div>
  <div class="email-box">Email Address</div>
  <div class="subscribe">Subscribe Now</div>
</footer>
<div class="copyright abs">Copyright © 2021 <b>Beacon Ridge Security Group</b>. All rights reserved.</div>

</body>
</html>
```